Wedding Invitation for a wedding at home - personal, romantic event

Want a wedding invitation that is to be printed onto card.
Size to be 148mm x 210mm
For it to open like a book not tent card
Have a picture of a house that I want to be the front cover.
I've attached 2 pictures. I like the picture without the man but with the grass
For the photo to become a drawing and the colours to be brighter.
If you could use the picture of us and get us in one of the windows.
If you could put the picture of the dog maybe somewhere on the grass.
Love the colour of the sky in the picture of the beach

Words to be on the inside of the card:
Together with our families
You are invited to the Wedding Reception of Polly Faraway and Ned Bramwick
On Saturday 9th of September 2017 at 6pm
At Bramwick's Keep, 41b, Fennow Crescent, Camberley, Surrey, GU19 7QX
Carriages at 1am
RSVP by Friday 27th of July to 07712 958 061

Words on the Back page:
With all that we have, we've been truly blessed.
Your presence and prayers are all that we request.
But if you desire to give nonetheless,
Monetary gift is one we suggest.

If the pages can be white.
Writing in gold
gold border on all pages

Target Market(s)

Wedding guests

Industry/Entity Type

Wedding

Font styles to use
Script

Requirements
Must have
• Romantic feel. Our wedding colours are white, gold and rose gold.
• Designer to be creative and I do not have much inspiration.
Nice to have
• metallic colours
• Maybe have MR & MRS in gold metallic on the front page

```html
<!DOCTYPE html>
<html lang="en">
<head>
<meta charset="utf-8">
<title>Polly &amp; Ned – Wedding Reception Invitation</title>
<link href="https://fonts.googleapis.com/css2?family=Handlee&display=swap" rel="stylesheet">
<style>
  :root {
    --backdrop: #4a2f20;
    --cream: #ecd8bb;
    --cream-light: #f5e9d7;
    --white: #ffffff;
    --ink: #7a4a2a;
    --ink-soft: #8b5a3a;
    --fold: #8e8e8e;
    --dot: #e5b79c;
    --house-sky: #f6dcb8;
    --house-brick: #a2523f;
    --photo-warm: #b98a74;
    --photo-light: #f1e1d6;
  }
  * { margin: 0; padding: 0; box-sizing: border-box; }
  html, body { width: 1200px; height: 1000px; overflow: hidden; }
  body {
    background: var(--backdrop);
    position: relative;
    font-family: "Handlee", cursive;
    color: var(--ink);
  }
  .spread {
    position: absolute;
    left: 75px;
    width: 1045px;
    height: 377px;
    overflow: hidden;
    box-shadow: 0 2px 6px rgba(0,0,0,.45);
  }
  .spread--outer { top: 113px; }
  .spread--inner { top: 530px; }
  .panel { position: absolute; top: 0; height: 100%; }
  .panel--left { left: 0; width: 523px; }
  .panel--right { left: 523px; width: 522px; }
  .fold {
    position: absolute; left: 523px; width: 1px; background: var(--fold);
  }
  .fold--top { top: 0; height: 48px; }
  .fold--bottom { bottom: 0; height: 60px; }

  /* outer spread */
  .back-page { background: linear-gradient(90deg, var(--cream) 0%, var(--cream-light) 100%); }
  .verse {
    position: absolute; top: 100px; left: 0; width: 100%;
    text-align: center; font-size: 22px; line-height: 43px;
    color: var(--ink-soft);
    text-shadow: 0 1px 1px rgba(255,255,255,.7), 0 -1px 1px rgba(90,50,20,.25);
  }
  .cover { background: linear-gradient(90deg, var(--cream) 0%, var(--white) 35%, var(--white) 100%); }
  .cover__house { position: absolute; right: 0; top: 0; }
  .cover__names {
    position: absolute; left: 105px; top: 222px;
    font-size: 66px; line-height: 56px; color: var(--ink);
    text-shadow: 1px 2px 2px rgba(90,50,20,.35);
  }
  .cover__names span { display: block; padding-left: 110px; }

  /* inner spread */
  .invite { background: linear-gradient(90deg, var(--white) 0%, var(--white) 88%, var(--cream-light) 100%); }
  .invite__frame { position: absolute; left: 0; top: 0; }
  .invite__text {
    position: absolute; top: 22px; left: 0; width: 540px; text-align: center;
  }
  .invite__lead { font-size: 17px; line-height: 27px; }
  .invite__couple { font-size: 30px; margin-top: 14px; line-height: 40px; }
  .invite__details { font-size: 20px; line-height: 31px; margin-top: 20px; }
  .invite__footer {
    position: absolute; top: 326px; left: 0; width: 520px; text-align: center;
    font-size: 15px; line-height: 21px; letter-spacing: .5px;
  }
  .portrait-page { background: linear-gradient(90deg, var(--white) 0%, var(--cream) 45%, var(--cream) 100%); }
  .portrait-page svg { position: absolute; left: 0; top: 0; }
</style>
</head>
<body>

<section class="spread spread--outer">
  <div class="panel panel--left back-page">
    <p class="verse">
      With all that we have, we’ve been truly blessed.<br>
      Your presence and prayers are all that we request.<br>
      But if you desire to give nonetheless,<br>
      Monetary gift is one we suggest.
    </p>
  </div>
  <div class="panel panel--right cover">
    <svg class="cover__house" width="270" height="280" viewBox="0 0 270 280" role="img" aria-label="Soft-edged illustration of the couple's red-brick house under a warm sky">
      <defs>
        <radialGradient id="houseFade" cx="0.55" cy="0.4" r="0.6">
          <stop offset="0" stop-color="var(--house-brick)" stop-opacity=".85"/>
          <stop offset="0.6" stop-color="var(--house-brick)" stop-opacity=".6"/>
          <stop offset="1" stop-color="var(--white)" stop-opacity="0"/>
        </radialGradient>
        <linearGradient id="houseSky" x1="0" y1="0" x2="0" y2="1">
          <stop offset="0" stop-color="var(--house-sky)"/>
          <stop offset="0.4" stop-color="#dfe6ea"/>
          <stop offset="1" stop-color="#c9c6bf"/>
        </linearGradient>
      </defs>
      <ellipse cx="160" cy="125" rx="160" ry="150" fill="url(#houseSky)" opacity=".85"/>
      <ellipse cx="160" cy="130" rx="150" ry="140" fill="url(#houseFade)"/>
    </svg>
    <div class="cover__names">Polly<span>&amp; Ned</span></div>
  </div>
  <div class="fold fold--top"></div>
  <div class="fold fold--bottom"></div>
</section>

<section class="spread spread--inner">
  <div class="panel panel--left invite">
    <svg class="invite__frame" width="523" height="377" viewBox="0 0 523 377" aria-hidden="true">
      <ellipse cx="270" cy="158" rx="242" ry="155" fill="none" stroke="var(--dot)" stroke-width="2.4" stroke-dasharray="0.1 6" stroke-linecap="round"/>
    </svg>
    <div class="invite__text">
      <p class="invite__lead">Together with our families<br>You are invited to the Wedding Reception of</p>
      <p class="invite__couple">Polly Faraway and Ned Bramwick</p>
      <p class="invite__details">
        On Saturday 9th of September 2017 at 6pm<br>
        At Bramwick’s Keep,<br>
        41b, Fennow Crescent,<br>
        Camberley, Surrey, GU19 7QX
      </p>
    </div>
    <p class="invite__footer">CARRIAGES AT 1AM<br>RSVP BY FRIDAY 27TH OF JULY TO 07712 958 061</p>
  </div>
  <div class="panel panel--right portrait-page">
    <svg width="522" height="377" viewBox="0 0 522 377">
      <defs>
        <linearGradient id="portraitTone" x1="0" y1="0" x2="1" y2="1">
          <stop offset="0" stop-color="var(--photo-light)"/>
          <stop offset="0.5" stop-color="var(--photo-warm)"/>
          <stop offset="1" stop-color="#8d7a72"/>
        </linearGradient>
      </defs>
      <ellipse cx="252" cy="184" rx="137" ry="187" fill="none" stroke="var(--dot)" stroke-width="2.4" stroke-dasharray="0.1 6" stroke-linecap="round"/>
      <ellipse cx="257" cy="184" rx="126" ry="179" fill="url(#portraitTone)" role="img" aria-label="Oval photograph of the couple together"/>
    </svg>
  </div>
  <div class="fold fold--top"></div>
  <div class="fold fold--bottom"></div>
</section>

</body>
</html>
```